www.tralvexhealth.com

We are a company that is in the business of extending the life of surgical equipment by repairing or refurbishing equipment to save hospitals, surgery centers and clinics money. We call ourselves Basset Medical Corporation. We are in need of a website that delivers the "feel" of what of we do everyday. A website that explains our services but at the same time has a touch that is different from the rest. Many companies repair but their websites may not "pull" customers to inquire, we need that punch. At this time we are not looking for e-commerce but would like the option of adding that in the future. We do sell new and used equipment, so we like to be able to highlight those manufacturers on our site. We would like the website to have enough layouts for pictures to describe what we repair.
Target Market(s)
Biomedical Technicians and Managers, Hospital Purchasing Departments, OR Managers, type of facilities that our customer exists in, hospitals, surgery centers, clinics, animal hospitals
Industry/Entity Type
E-Commerce
Requirements
Must have
- An easy to navigate website, modern looking.
Easy to modify with pictures and or additional web pages
The winning designer to be available for future modifications and changes
Website to be unique compared to our competition, which are numerous
Nice to have
- E-Commerce capability

```html
<!DOCTYPE html>
<html lang="en">
<head>
<meta charset="utf-8">
<title>Basset Medical Corporation</title>
<link href="https://fonts.googleapis.com/css2?family=Arimo:wght@400;700&family=PT+Sans:wght@400;700&display=swap" rel="stylesheet">
<style>
:root{
  --page:#efefef;
  --white:#ffffff;
  --soft:#f7f7f7;
  --ink:#2b2b2b;
  --text:#333333;
  --green:#7ab317;
  --blue:#1a7fc8;
  --blue-light:#2b9bd9;
  --blue-dark:#0f5b93;
  --link:#1d7cc4;
  --foot:#3d3d3d;
  --foot-band:#5b5b5b;
  --foot-text:#d9d9d9;
}
*{box-sizing:border-box;margin:0;padding:0}
html,body{width:1151px;height:1200px;overflow:hidden}
body{background:var(--page);font-family:"Arimo",Arial,sans-serif;color:var(--text);position:relative}
.abs{position:absolute}
.column{left:98px;top:0;width:955px;height:1084px;background:var(--white);box-shadow:0 0 8px rgba(0,0,0,.12)}
.brand{left:113px;top:30px;display:flex;align-items:center;gap:10px}
.brand-dot{width:44px;height:44px;border-radius:50%;background:var(--blue)}
.brand-name{font-family:"PT Sans",sans-serif;font-weight:700;font-size:22px;color:var(--green);line-height:1.1}
.appointment{left:775px;top:24px;width:235px;height:69px;border:1px solid #bbb;border-radius:5px;background:linear-gradient(#8ee04a,#4aac1c);display:flex;align-items:center}
.appointment-text{font-family:"PT Sans",sans-serif;color:#fff;padding-left:18px;line-height:1}
.appointment-text small{display:block;font-size:15px}
.appointment-text b{font-size:21px;letter-spacing:.3px}
.appointment svg{position:absolute;right:2px;top:2px}
.nav{left:101px;top:112px;width:926px;height:45px;border-top:1px solid #e6e6e6;display:flex;align-items:center;font-weight:700;font-size:13.5px;letter-spacing:.4px;color:#333}
.nav a{color:inherit;text-decoration:none;position:relative;height:100%;display:flex;align-items:center}
.nav .active::before{content:"";position:absolute;left:-15px;right:-22px;top:-2px;height:3px;background:var(--green)}
.social{left:914px;top:118px;display:flex;gap:10px}
.social span{width:32px;height:32px;border-radius:50%;background:#c9c9c9}
.band{left:0;top:172px;width:1151px;height:355px;background:var(--blue-light)}
.frame{left:80px;top:155px;width:992px;height:355px;background:var(--blue)}
.fold-l{left:80px;top:510px;border-top:16px solid var(--blue-dark);border-left:18px solid transparent}
.fold-r{left:1054px;top:510px;border-top:16px solid var(--blue-dark);border-right:18px solid transparent}
.hero{left:117px;top:166px;width:914px;height:330px;background:linear-gradient(90deg,#cfd6dc 0%,#e8dcc4 45%,#e8b868 75%,#b99a80 100%)}
.card{top:546px;width:200px}
.thumb{width:187px;height:108px;border:1px solid #ccc;padding:4px;background:#fff}
.thumb div{width:100%;height:100%}
.card h3{margin-top:13px;font-size:12.5px;font-weight:700;color:var(--link);letter-spacing:.2px}
.card p{font-size:12px;line-height:17.5px;margin-top:2px;color:#333}
.more{display:inline-block;margin-top:8px;padding:6px 9px;font-size:11.5px;font-weight:700;color:#fff;background:linear-gradient(#2a8fd8,#0d64ad);border-radius:4px;border-bottom:2px solid #0a4a80}
.welcome{left:98px;top:803px;width:955px;height:265px;background:var(--soft)}
.welcome h1{position:absolute;left:14px;top:20px;font-family:"PT Sans",sans-serif;font-weight:400;font-size:24px;color:var(--ink)}
.welcome h1 span{color:#2577bf;font-weight:700}
.welcome .copy{position:absolute;left:15px;top:56px;width:620px;font-size:12px;line-height:19.2px;color:#333}
.welcome .copy p+p{margin-top:19px}
.action{left:756px;width:254px;height:38px;border-radius:3px;display:flex;align-items:center;padding-left:12px;gap:12px;font-family:"PT Sans",sans-serif;font-weight:700;font-size:13.5px;color:#fff}
.action svg.chev{margin-left:auto;margin-right:10px}
.quote{top:823px;background:linear-gradient(#3f8ed6,#2369b3);border-bottom:3px solid #1b558f}
.invoice{top:885px;background:linear-gradient(#4cae3e,#2f8a2a);border-bottom:3px solid #25691f}
.contact{top:948px;background:linear-gradient(#ee3a3f,#d01e25);border-bottom:3px solid #a8151a}
.shop{top:1008px;background:linear-gradient(#f1b52a,#d9930a);border-bottom:3px solid #ad7308}
.foot-band{left:0;top:1068px;width:1151px;height:132px;background:var(--foot-band)}
.footer{left:80px;top:1084px;width:992px;height:116px;background:var(--foot)}
.foot-brand{left:115px;top:1108px;display:flex;align-items:center;gap:10px}
.foot-brand .brand-dot{background:#9a9a9a}
.foot-brand .brand-name{color:#b5b5b5}
.foot-links{right:102px;top:1109px;text-align:right;font-size:12px;line-height:23px;color:var(--foot-text);letter-spacing:.3px}
</style>
</head>
<body>
<div class="abs column"></div>

<header>
  <div class="abs brand">
    <span class="brand-dot"></span>
    <span class="brand-name">Basset Medical<br>Corporation</span>
  </div>
  <div class="abs appointment">
    <div class="appointment-text"><small>Click Here to Request a</small><b>REPAIR QUOTE</b></div>
    <svg width="58" height="64" viewBox="0 0 58 64" aria-hidden="true">
      <circle cx="34" cy="32" r="27" fill="#f4f4f4" stroke="#999" stroke-width="2"/>
      <line x1="34" y1="32" x2="34" y2="14" stroke="#333" stroke-width="2"/>
      <line x1="34" y1="32" x2="46" y2="40" stroke="#333" stroke-width="2"/>
    </svg>
  </div>
  <nav class="abs nav">
    <a class="active" href="#" style="margin-left:15px">HOME</a>
    <a href="#" style="margin-left:59px">ABOUT</a>
    <a href="#" style="margin-left:59px">SERVICES</a>
    <a href="#" style="margin-left:57px">REPAIRS</a>
    <a href="#" style="margin-left:45px">EQUIPMENT</a>
    <a href="#" style="margin-left:45px">VIDEOS</a>
    <a href="#" style="margin-left:50px">CONTACT US</a>
  </nav>
  <div class="abs social" aria-label="Social links"><span></span><span></span><span></span></div>
</header>

<div class="abs band"></div>
<div class="abs frame"></div>
<div class="abs fold-l"></div>
<div class="abs fold-r"></div>
<div class="abs hero" role="img" aria-label="Technician at a workbench repairing a surgical instrument"></div>

<section>
  <article class="abs card" style="left:128px">
    <div class="thumb"><div role="img" aria-label="Rigid surgical scopes laid out for inspection" style="background:linear-gradient(#c3ccd4,#6f7f8e)"></div></div>
    <h3>Surgical Scope Repair</h3>
    <p>Precision rebuilds return scopes to factory specs</p>
    <span class="more">Learn More</span>
  </article>
  <article class="abs card" style="left:357px">
    <div class="thumb"><div role="img" aria-label="Surgical power drill on a repair bench" style="background:linear-gradient(#c9a57a,#6d5540)"></div></div>
    <h3>Power Tool Refurbishing</h3>
    <p>Drills, saws and handpieces tested and rebuilt for a fraction of new cost.</p>
    <span class="more">Learn More</span>
  </article>
  <article class="abs card" style="left:595px">
    <div class="thumb"><div role="img" aria-label="Biomedical technician testing equipment" style="background:linear-gradient(#ddd3c6,#7c6a60)"></div></div>
    <h3>Certified Repair Programs</h3>
    <p>Every repair is tested, documented and backed by our service warranty.</p>
    <span class="more">Learn More</span>
  </article>
  <article class="abs card" style="left:828px">
    <div class="thumb"><div role="img" aria-label="Shelf of new and used surgical equipment" style="background:linear-gradient(#bcd0dc,#6f84a6)"></div></div>
    <h3>New &amp; Used Equipment</h3>
    <p>Quality units from leading makers.</p>
    <span class="more">Learn More</span>
  </article>
</section>

<section class="abs welcome">
  <h1>Welcome to <span>Basset Medical Corporation</span></h1>
  <div class="copy">
    <p>Basset Medical Corporation extends the life of surgical equipment. Our technicians repair and refurbish scopes, power tools, instruments and OR devices so hospitals, surgery centers, clinics and animal hospitals can keep working gear in service and save money. Every unit is inspected, rebuilt to manufacturer standards and tested before it leaves our bench. Biomedical teams, OR managers and purchasing departments rely on our fast turnaround, loaner options and clear quotes to keep procedures on schedule without the cost of buying new.</p>
    <p>We also sell new and used equipment from trusted manufacturers, so you can replace, upgrade or add capacity with one call to a partner who knows your equipment.</p>
  </div>
</section>

<a class="abs action quote">
  <svg width="30" height="24" viewBox="0 0 30 24" aria-hidden="true"><path d="M6 18l9-9M13 5a5 5 0 0 0 6 6l4-4-2-2-3 1-1-3z" fill="none" stroke="#fff" stroke-width="2"/></svg>
  Request a Repair
  <svg class="chev" width="12" height="18" viewBox="0 0 12 18" aria-hidden="true"><path d="M2 2l7 7-7 7" fill="none" stroke="#16457a" stroke-width="3"/></svg>
</a>
<a class="abs action invoice">
  <svg width="30" height="24" viewBox="0 0 30 24" aria-hidden="true"><rect x="8" y="2" width="14" height="20" rx="2" fill="none" stroke="#fff" stroke-width="2"/><path d="M11 8h8M11 12h8M11 16h8" stroke="#fff" stroke-width="1.5"/></svg>
  Pay My Invoice
  <svg class="chev" width="12" height="18" viewBox="0 0 12 18" aria-hidden="true"><path d="M2 2l7 7-7 7" fill="none" stroke="#1f5a1a" stroke-width="3"/></svg>
</a>
<a class="abs action contact">
  <svg width="30" height="24" viewBox="0 0 30 24" aria-hidden="true"><circle cx="15" cy="12" r="9" fill="none" stroke="#fff" stroke-width="2"/><circle cx="15" cy="12" r="3.5" fill="none" stroke="#fff" stroke-width="2"/></svg>
  Contact Us
  <svg class="chev" width="12" height="18" viewBox="0 0 12 18" aria-hidden="true"><path d="M2 2l7 7-7 7" fill="none" stroke="#8e1115" stroke-width="3"/></svg>
</a>
<a class="abs action shop">
  <svg width="30" height="24" viewBox="0 0 30 24" aria-hidden="true"><path d="M4 4h4l3 12h12l2-8H10" fill="none" stroke="#fff" stroke-width="2"/><circle cx="12" cy="20" r="2" fill="#fff"/><circle cx="21" cy="20" r="2" fill="#fff"/></svg>
  Shop Equipment
  <svg class="chev" width="12" height="18" viewBox="0 0 12 18" aria-hidden="true"><path d="M2 2l7 7-7 7" fill="none" stroke="#b0480a" stroke-width="3"/></svg>
</a>

<footer>
  <div class="abs foot-band"></div>
  <div class="abs footer"></div>
  <div class="abs foot-brand">
    <span class="brand-dot"></span>
    <span class="brand-name">Basset Medical<br>Corporation</span>
  </div>
  <div class="abs foot-links">
    Home &nbsp;~&nbsp; Who We Are &nbsp;~&nbsp; Repairs &nbsp;~&nbsp; Equipment &nbsp;~&nbsp; Contact Us<br>
    Basset Medical Corporation, Copyright © 2013, Privacy Policy
  </div>
</footer>
</body>
</html>
```